Veranaxis Business Card and Letter Head

We are a leadership assessment consultancy based in Sydney, Australia. We help executive-level decison-makers select leaders for more senior level roles in corporate and government organisations. Our methodology is based on the latest research from the field of neuroscience.
We need a business card design and matching letter head that presents our company, Veranaxis, as a:
1. trusted adviser to senior executive-level decison makers
2. niche consultancy who are experts in the field of assessing leadership talent
3. results-focused solution provider who balance scientific methods with pragmatic solutions
The following company details should be used in all designs:
Company Name: Veranaxis
Details (for business card):
Daniel Prescott
Senior Assessment Advisor
Level 29, Brenning Tower
7 Brenning Square
Sydney, NSW 2000 Australia
Phone: 1300 482 716
Mobile: 0412 573 208
Email: daniel.prescott@veranaxis.com.au
Website: veranaxis.com.au
I have attached the logo for Veranaxis (for both a white and black background) - your business card and letter head designs must incoporate this logo and colour scheme.
Thanks for your interest in this project, I'm looking forward to receiving your ideas.
Regards,
Daniel
Executive-level decison-makers in corporate and government organisations (e.g., CEO, VP, Head of Human Resources)
Leadership

```html
<!DOCTYPE html>
<html lang="en">
<head>
<meta charset="utf-8">
<title>Veranaxis Business Card</title>
<link rel="stylesheet" href="https://fonts.googleapis.com/css2?family=PT+Sans+Narrow:wght@400;700&family=Raleway:wght@300;400&display=swap">
<style>
  :root {
    --stage: #e4e4e4;
    --charcoal: #48484a;
    --charcoal-deep: #3a3a3c;
    --red: #b8321f;
    --paper: #f1f1ef;
    --ink: #3a3a3c;
    --muted: #6b6b6d;
    --white: #ffffff;
    --soft-white: #d9d9d9;
  }
  * { margin: 0; padding: 0; box-sizing: border-box; }
  html, body { width: 1200px; height: 900px; overflow: hidden; }
  body {
    background: var(--stage);
    font-family: "PT Sans Narrow", "Arial Narrow", sans-serif;
    position: relative;
  }
  .card {
    position: absolute;
    left: 260px;
    width: 680px;
    height: 390px;
    overflow: hidden;
    box-shadow: 0 6px 18px rgba(0,0,0,0.18);
  }

  /* contact side */
  .card-back { top: 40px; background: var(--charcoal); }
  .back-edge {
    position: absolute; left: 0; top: 0; bottom: 0; width: 18px;
    background: var(--paper);
  }
  .back-brand {
    position: absolute; left: 64px; top: 52px;
    display: flex; align-items: center; gap: 14px;
  }
  .brand-square { display: block; width: 22px; height: 22px; background: var(--red); }
  .back-brand .brand-name {
    font-weight: 700; font-size: 44px; line-height: 1; color: var(--white);
  }
  .back-rule {
    position: absolute; left: 64px; top: 132px; width: 380px; height: 2px;
    background: var(--white);
  }
  .back-rule::after {
    content: ""; position: absolute; left: 0; top: 0; width: 60px; height: 2px;
    background: var(--red);
  }
  .contact {
    position: absolute; left: 64px; top: 156px; right: 40px;
    color: var(--soft-white); font-size: 17px; line-height: 1.4;
  }
  .contact-name { color: var(--red); font-weight: 700; font-size: 26px; line-height: 1.1; }
  .contact-title { color: var(--white); margin-bottom: 16px; }
  .contact-columns { display: flex; gap: 48px; }

  /* brand side */
  .card-front { top: 470px; background: var(--paper); }
  .front-base {
    position: absolute; left: 0; right: 0; bottom: 0; height: 64px;
    background: var(--charcoal);
  }
  .front-accent {
    position: absolute; left: 0; right: 0; bottom: 64px; height: 8px;
    background: var(--red);
  }
  .front-lockup {
    position: absolute; left: 0; right: 0; top: 104px;
    display: flex; flex-direction: column; align-items: center;
  }
  .front-brand { display: flex; align-items: center; gap: 18px; }
  .front-brand .brand-square { width: 30px; height: 30px; background: var(--red); }
  .front-brand .brand-name {
    font-weight: 700; font-size: 76px; line-height: 1; color: var(--ink);
  }
  .tagline {
    margin-top: 12px;
    font-family: "Raleway", "Helvetica Neue", sans-serif;
    font-weight: 400; font-size: 16px; letter-spacing: 2px;
    color: var(--muted); text-transform: uppercase;
  }
</style>
</head>
<body>

<section class="card card-back" aria-label="Business card, contact side">
  <div class="back-edge"></div>
  <div class="back-brand">
    <span class="brand-square"></span>
    <span class="brand-name">Veranaxis</span>
  </div>
  <div class="back-rule"></div>
  <div class="contact">
    <p class="contact-name">Daniel Prescott</p>
    <p class="contact-title">Senior Assessment Advisor</p>
    <div class="contact-columns">
      <div>
        <p>Phone: 1300 482 716</p>
        <p>Mobile: 0412 573 208</p>
        <p>Level 29, Brenning Tower</p>
        <p>7 Brenning Square, Sydney, NSW 2000 Australia</p>
      </div>
      <div>
        <p>Web: www.veranaxis.com.au</p>
        <p>Email: daniel.prescott@veranaxis.com.au</p>
      </div>
    </div>
  </div>
</section>

<section class="card card-front" aria-label="Business card, brand side">
  <div class="front-lockup">
    <div class="front-brand">
      <span class="brand-square"></span>
      <span class="brand-name">Veranaxis</span>
    </div>
    <p class="tagline">Assessing Leaders With Evidence</p>
  </div>
  <div class="front-accent"></div>
  <div class="front-base"></div>
</section>

</body>
</html>
```